Valu Tea Label & packaging for a premium tea brand. For local and global market

Create a look and feel for a box and rectangle tin. We are looking for a luxe packaging design for a new tea brand based in Kenya called 'Valu Tea'. Kenya is home to the finest teas in the world and Valu tea looks to embody that fact. Valu Tea uses the most premium of Kenyan Tea, Black tea, Purple tea, White Tea, Green tea, Hibiscus Tea and Moringa Tea. Valu Tea is handpicked from Kenya's highlands. This project will include the look and feel of the different teas described above. The copy on the main face of the box should read 'Premium Kenyan Tea' The box will contain 25 tagged tea bags, with a net weight of 50 gms.

On one side of the box will read 'packaging instructions' To fully savour this Valu premium tea, use one tea bag for each cup, add some freshly bolded water and wait for 2 minutes as you enjoy the sweet aroma of our tea, stir and serve' Ingredients : Black Tea, and for the others the same : Hibiscus Tea, Green Tea, Purple Tea, White tea. should also feature on the label: Produce of Kenya.

Target Market(s)

Premium

Industry/Entity Type

Agribusiness

Font styles to use
Script

Colors

Designer to choose colors to be used in the design.

Requirements
Must have
• Luxe look and feel
Nice to have
• I have attached the Valu tea logo and images of brands I'd lile the designer to be inspired by.
Should not have
• Green and yellow colours

```html
<!DOCTYPE html>
<html lang="en">
<head>
<meta charset="utf-8">
<title>Valu Tea – Premium Kenyan Black Tea Label</title>
<link rel="stylesheet" href="https://fonts.googleapis.com/css2?family=Cinzel:wght@500;600;700&display=swap">
<style>
  :root {
    --page: #ffffff;
    --marble-dark: #0b0b0a;
    --marble-mid: #2a211b;
    --marble-copper: #b7825a;
    --copper-light: #e4b58e;
    --copper: #c98e63;
    --copper-deep: #a4673f;
    --label-white: #ffffff;
    --ink: #221f20;
    --brand-gold: #e8a417;
  }
  * { margin: 0; padding: 0; box-sizing: border-box; }
  html, body {
    width: 1200px; height: 960px; overflow: hidden;
    background: var(--page);
  }
  .canvas { position: relative; width: 1200px; height: 960px; }

  .marble-ground {
    position: absolute; left: 165px; top: 206px; width: 874px; height: 503px;
    background:
      radial-gradient(ellipse 260px 90px at 82% 8%, var(--marble-copper) 0%, transparent 70%),
      radial-gradient(ellipse 300px 70px at 40% 95%, var(--marble-copper) 0%, transparent 70%),
      radial-gradient(ellipse 90px 160px at 3% 45%, #7a5338 0%, transparent 75%),
      linear-gradient(135deg, var(--marble-dark) 0%, var(--marble-mid) 50%, var(--marble-dark) 100%);
  }
  .copper-frame {
    position: absolute; left: 194px; top: 259px; width: 815px; height: 397px;
    background: linear-gradient(120deg, var(--copper-deep) 0%, var(--copper-light) 30%, var(--copper) 55%, var(--copper-deep) 80%, var(--copper) 100%);
  }
  .label-panel {
    position: absolute; left: 213px; top: 282px; width: 774px; height: 353px;
    background: var(--label-white);
  }
  .label-border {
    position: absolute; left: 14px; top: 8px; width: 750px; height: 331px;
    border: 6px solid var(--ink);
  }
  .brand-mark {
    position: absolute; left: 327px; top: 31px; width: 104px; height: 85px;
    background: var(--ink);
    display: flex; align-items: center; justify-content: center;
    font-family: "Cinzel", serif; font-weight: 600; font-size: 24px;
    letter-spacing: 1px; color: var(--brand-gold);
  }
  .product-title {
    position: absolute; left: 0; right: 0; top: 150px; text-align: center;
    font-family: "Cinzel", serif; color: var(--ink);
  }
  .product-title .origin {
    display: block; font-size: 20px; font-weight: 700; letter-spacing: 0.5px; line-height: 24px;
  }
  .product-title .variety {
    display: block; font-size: 56px; font-weight: 700; line-height: 56px; letter-spacing: 0;
  }
  .net-weight {
    position: absolute; right: 34px; top: 299px; text-align: center;
    font-family: "Cinzel", serif; color: var(--ink); font-weight: 700;
  }
  .net-weight .caption { display: block; font-size: 11px; letter-spacing: 0.6px; line-height: 14px; }
  .net-weight .amount { display: block; font-size: 21px; line-height: 24px; }
</style>
</head>
<body>
<div class="canvas">
  <div class="marble-ground" role="img" aria-label="Black marble texture with copper veins"></div>
  <div class="copper-frame" role="img" aria-label="Brushed copper foil frame"></div>
  <div class="label-panel">
    <div class="label-border"></div>
    <div class="brand-mark">VALU</div>
    <h1 class="product-title">
      <span class="origin">PREMIUM KENYAN</span>
      <span class="variety">BLACK TEA</span>
    </h1>
    <div class="net-weight">
      <span class="caption">NET WEIGHT</span>
      <span class="amount">50 GMS</span>
    </div>
  </div>
</div>
</body>
</html>
```